A picture showing off our Million Dollar Renovation Update at Meadow Falls Splashpark Lodge

Use the uploaded images to develop a picture at least 1366x512 with text saying - Check out our Million Dollar Renovation - I have uploaded alot please use the best to show off . It will go as the hero picture on this website https://meadowfallslodge.example/ - would also to use in social in a "splash" manner to show off updates

Target Market(s)

visitors to our website and past guest

Industry/Entity Type

Hotel

Requirements
Must have
• Check out Our Million Dollar Renovation!
Nice to have
• pictures

```html
<!DOCTYPE html>
<html lang="en">
<head>
<meta charset="utf-8">
<title>Meadow Falls Splashpark Lodge – Million Dollar Renovation Hero</title>
<link href="https://fonts.googleapis.com/css2?family=Jost:ital,wght@0,300;0,400;0,500;1,400&family=Roboto:wght@400;500;700&display=swap" rel="stylesheet">
<style>
  :root {
    --sheet-bg: #ffffff;
    --ink: #2b2b2b;
    --label: #555555;
    --navy: #23335f;
    --orange: #f47a20;
    --orange-bright: #ff7a1a;
    --header-bg: #eff0f8;
    --room-dark: #2a2a2c;
    --room-mid: #4a4b4e;
    --room-wall: #4f8a3a;
    --room-bed: #5e8f7a;
    --white: #ffffff;
    --footer: #000000;
  }
  * { box-sizing: border-box; margin: 0; padding: 0; }
  html, body {
    width: 892px; height: 1200px; overflow: hidden;
    background: var(--sheet-bg);
    font-family: "Jost", "Futura", sans-serif;
  }
  .sheet { position: relative; width: 892px; height: 1200px; }

  /* Hero banner component */
  .hero { position: absolute; overflow: hidden; }
  .hero__art { position: absolute; inset: 0; width: 100%; height: 100%; display: block; }
  .hero__copy { position: absolute; color: var(--white); }
  .hero__kicker { font-style: italic; font-weight: 400; letter-spacing: 0.02em; text-transform: uppercase; }
  .hero__headline { color: var(--orange); font-weight: 400; text-transform: uppercase; letter-spacing: 0.04em; }

  .hero--standalone { left: 52px; top: 75px; width: 787px; height: 295px; }
  .hero--standalone .hero__copy { left: 59px; top: 50px; }
  .hero--standalone .hero__kicker { font-size: 20px; line-height: 1; }
  .hero--standalone .hero__headline { font-size: 29px; line-height: 42px; margin-top: 14px; }

  .spec-label {
    position: absolute; left: 52px;
    font-family: "Jost", sans-serif; font-weight: 300;
    font-size: 12px; letter-spacing: 0.28em; color: var(--label);
    text-transform: uppercase;
  }
  .spec-label--size { top: 398px; }
  .spec-label--mockup { top: 983px; }

  /* Website mockup */
  .site {
    position: absolute; left: 99px; top: 519px; width: 694px; height: 434px;
    background: var(--white);
    box-shadow: 0 18px 30px rgba(0,0,0,0.28);
    font-family: "Roboto", sans-serif;
  }
  .site__header {
    position: relative; height: 85px; background: var(--header-bg);
  }
  .site__brand {
    position: absolute; left: 150px; top: 22px;
    display: flex; align-items: center; gap: 8px;
    color: var(--navy); font-family: "Jost", sans-serif; font-weight: 500;
    font-size: 17px; line-height: 20px; width: 200px;
  }
  .site__brand-dot {
    flex: none; width: 34px; height: 34px; border-radius: 50%; background: var(--navy);
  }
  .site__phone {
    position: absolute; right: 72px; top: 33px;
    color: var(--navy); font-weight: 700; font-size: 16px;
  }
  .site__nav {
    position: relative; height: 27px; background: var(--navy);
    display: flex; align-items: center;
  }
  .site__nav-link {
    position: absolute; top: 0; line-height: 27px;
    color: var(--orange-bright); font-size: 11.5px; font-weight: 500;
    transform: translateX(-50%); white-space: nowrap;
  }
  .site__nav-cta {
    position: absolute; right: 0; top: 0; width: 141px; height: 27px;
    background: var(--orange-bright); border: 2px solid var(--orange);
    color: var(--navy); font-size: 11.5px; font-weight: 500;
    display: flex; align-items: center; justify-content: center;
  }
  .hero--site { left: 0; top: 112px; width: 694px; height: 261px; }
  .hero--site .hero__copy { left: 52px; top: 45px; }
  .hero--site .hero__kicker { font-size: 18px; line-height: 1; }
  .hero--site .hero__headline { font-size: 25px; line-height: 37px; margin-top: 11px; }

  .booking {
    position: absolute; left: 0; right: 0; top: 373px; height: 61px;
    display: flex; align-items: center; justify-content: center; gap: 9px;
    font-size: 9px; color: var(--navy);
  }
  .booking__field { display: flex; align-items: center; gap: 4px; }
  .booking__input {
    border: 1px solid #c8c8c8; background: #fafafa; color: #333;
    font-size: 8px; padding: 1px 3px; line-height: 10px;
  }
  .booking__input--date { width: 68px; }
  .booking__input--num { width: 14px; text-align: center; }
  .booking__submit {
    background: var(--orange-bright); color: var(--navy);
    font-size: 10px; font-weight: 500; padding: 2px 4px; border: 1px solid #d8651a;
  }

  .sheet-footer {
    position: absolute; left: 0; bottom: 0; width: 892px; height: 101px;
    background: var(--footer);
  }
</style>
</head>
<body>
<main class="sheet">

  <section class="hero hero--standalone">
    <svg class="hero__art" viewBox="0 0 1366 512" preserveAspectRatio="none">
      <defs>
        <linearGradient id="room-a" x1="0" y1="0" x2="1" y2="0.3">
          <stop offset="0" stop-color="#1f1f21"/>
          <stop offset="0.35" stop-color="#3a3b3e"/>
          <stop offset="0.55" stop-color="#4d7f3a"/>
          <stop offset="0.75" stop-color="#5e8f7a"/>
          <stop offset="1" stop-color="#2c2a29"/>
        </linearGradient>
        <radialGradient id="lounge-a" cx="0.5" cy="0.5" r="0.6">
          <stop offset="0" stop-color="#8d7a66"/><stop offset="1" stop-color="#3e2f28"/>
        </radialGradient>
        <radialGradient id="bath-a" cx="0.5" cy="0.6" r="0.6">
          <stop offset="0" stop-color="#f3efe9"/><stop offset="1" stop-color="#b9ab98"/>
        </radialGradient>
      </defs>
      <rect width="1366" height="512" fill="url(#room-a)" role="img" aria-label="Renovated guest room with king bed, teal quilt and dark headboard"/>
      <rect width="700" height="512" fill="#000" opacity="0.35"/>
      <circle cx="915" cy="354" r="107" fill="url(#lounge-a)" stroke="#fff" stroke-width="10" role="img" aria-label="Suite sitting area with leather sofa"/>
      <circle cx="1222" cy="330" r="141" fill="url(#bath-a)" stroke="#fff" stroke-width="10" role="img" aria-label="Suite with freestanding soaking tub"/>
      <path d="M0 430 C300 330 700 470 1000 430 S1300 320 1366 350 V512 H0Z" fill="#fff"/>
      <path d="M0 465 C350 385 800 500 1100 468 S1330 415 1366 425 V512 H0Z" fill="#23335f"/>
      <path d="M0 492 C250 440 520 470 720 512 H0Z" fill="#f47a20"/>
    </svg>
    <div class="hero__copy">
      <p class="hero__kicker">Check out our</p>
      <h1 class="hero__headline">Million Dollar<br>Renovation</h1>
    </div>
  </section>

  <p class="spec-label spec-label--size">1366x512 px</p>

  <section class="site">
    <header class="site__header">
      <div class="site__brand"><span class="site__brand-dot"></span><span>Meadow Falls Splashpark Lodge</span></div>
      <div class="site__phone">1-800-555-0142</div>
    </header>
    <nav class="site__nav">
      <span class="site__nav-link" style="left:76px">Guest Rooms</span>
      <span class="site__nav-link" style="left:225px">Waterpark</span>
      <span class="site__nav-link" style="left:350px">Discounts</span>
      <span class="site__nav-link" style="left:483px">Recreation</span>
      <span class="site__nav-cta">Book Now!</span>
    </nav>

    <div class="hero hero--site">
      <svg class="hero__art" viewBox="0 0 1366 512" preserveAspectRatio="none">
        <defs>
          <linearGradient id="room-b" x1="0" y1="0" x2="1" y2="0.3">
            <stop offset="0" stop-color="#1f1f21"/>
            <stop offset="0.35" stop-color="#3a3b3e"/>
            <stop offset="0.55" stop-color="#4d7f3a"/>
            <stop offset="0.75" stop-color="#5e8f7a"/>
            <stop offset="1" stop-color="#2c2a29"/>
          </linearGradient>
          <radialGradient id="lounge-b" cx="0.5" cy="0.5" r="0.6">
            <stop offset="0" stop-color="#8d7a66"/><stop offset="1" stop-color="#3e2f28"/>
          </radialGradient>
          <radialGradient id="bath-b" cx="0.5" cy="0.6" r="0.6">
            <stop offset="0" stop-color="#f3efe9"/><stop offset="1" stop-color="#b9ab98"/>
          </radialGradient>
        </defs>
        <rect width="1366" height="512" fill="url(#room-b)" role="img" aria-label="Renovated guest room with king bed, teal quilt and dark headboard"/>
        <rect width="700" height="512" fill="#000" opacity="0.35"/>
        <circle cx="915" cy="354" r="107" fill="url(#lounge-b)" stroke="#fff" stroke-width="10" role="img" aria-label="Suite sitting area with leather sofa"/>
        <circle cx="1222" cy="330" r="141" fill="url(#bath-b)" stroke="#fff" stroke-width="10" role="img" aria-label="Suite with freestanding soaking tub"/>
        <path d="M0 430 C300 330 700 470 1000 430 S1300 320 1366 350 V512 H0Z" fill="#fff"/>
        <path d="M0 465 C350 385 800 500 1100 468 S1330 415 1366 425 V512 H0Z" fill="#23335f"/>
        <path d="M0 492 C250 440 520 470 720 512 H0Z" fill="#f47a20"/>
      </svg>
      <div class="hero__copy">
        <p class="hero__kicker">Check out our</p>
        <h2 class="hero__headline">Million Dollar<br>Renovation</h2>
      </div>
    </div>

    <form class="booking">
      <label class="booking__field">Arrival Date: <span class="booking__input booking__input--date">14/09/2018</span></label>
      <label class="booking__field"># of Nights: <span class="booking__input booking__input--num">2</span></label>
      <label class="booking__field"># of Adults: <span class="booking__input booking__input--num">2</span></label>
      <label class="booking__field"># of Children: <span class="booking__input booking__input--num">0</span></label>
      <span class="booking__submit">Book Direct!</span>
    </form>
  </section>

  <p class="spec-label spec-label--mockup">Mockup</p>

  <footer class="sheet-footer"></footer>
</main>
</body>
</html>
```